Veltrix Stationary

Design the stationary of Veltrix Promotions Group.

Veltrix is a BTL company, BTL meaning "below the line". In other words Veltrix is a Promotional Marketing company (the company that design the brands promotional activities).

The design should transmit creativity, agility, boldness.

I need:
* Bis Card
* Letter head
* Envelopes, both vertical and horizontal (for legal size), and letter envelope
* Folders
* PPT template (Title page and regular page)
* CD slip (CD envelope)
* ID card (employee card)

And what ever else you want to throw in.
Updates

Guys,

Something I missed from the brief.   The predominat color should be RED.

Also, have fun and play with the exclamation mark (!) of the logo. 

Hi guys, more comments:

Remember that Veltrix is a "creativity" agency, not in the advertising side but on the promotional side, and that should reflect on the stationary.

 I want a bold design.  Bold and yet crisp.

 

Guys, i just uploaded the Logo in AI format.

I Also uploaded the actual Veltrix Bis Card, wich I like.  So I will like to see some designs with that bis card approach.

Guys, I am so sorry, but I notice in your last post that I upladed a wrong design ("13154_marketing_group_veltrix_brief225630.ai").  The problem was that I asked the designer the file in AI format and he send me thw wrong file, and since I dont have Illustrator I could not verify it.

The differences are minor, I just already ask him the correct one (similar to the EPS file).

Sorry                                   

Just post the correct AI file : "Veltrix Logo.ai"

Reason: I'm expecting more designs to choose from and also I wont be available tomorrow to decide.

Reason: Sorry guys, but we are not there yet!

Target Market(s)

Marketing directors, Marketing Managers

Industry/Entity Type

Legal

Requirements
Must have
• Must work with the logo attached.
The predominat color should be RED.
Play and have fun with the exclamation mark (!).
Should not have
• * No old fonts

Should not be:
* boring
* Informal
* rigid

```html
<!DOCTYPE html>
<html lang="en">
<head>
<meta charset="utf-8">
<title>Veltrix Promotions Group — Stationery</title>
<link rel="stylesheet" href="https://fonts.googleapis.com/css2?family=Mulish:wght@400;600;700;800&display=swap">
<style>
:root{
  --red:#c3161f;
  --red-deep:#8e0e14;
  --red-light:#e0323a;
  --grey:#6d6e70;
  --ink:#231f20;
  --paper:#ffffff;
  --stage:#e6e6e6;
}
*{box-sizing:border-box;margin:0;padding:0}
html,body{width:1200px;height:808px;overflow:hidden}
body{background:var(--stage);font-family:"Mulish",sans-serif;color:var(--ink);position:relative}

.sheet{position:absolute;background:var(--paper);overflow:hidden;box-shadow:0 2px 8px rgba(0,0,0,.18)}
.band{position:absolute;left:0;bottom:0;width:100%;background:linear-gradient(180deg,var(--red-light),var(--red) 60%,var(--red-deep))}
.web{position:absolute;right:18px;color:#fff;font-size:8px;font-weight:600}

/* brand name */
.brand{font-weight:800;color:var(--ink);line-height:1;display:flex;align-items:flex-start;gap:5px}
.brand .name{display:flex;flex-direction:column}
.brand .word{letter-spacing:-.5px}
.brand .sub{letter-spacing:1.6px;margin-top:2px}
.brand .dot{border-radius:50%;background:var(--red);flex:none}
.brand.on-red{color:#fff}
.brand.on-red .dot{background:#fff}

/* business cards */
.card{top:40px;width:250px;height:143px}
.card-front{left:40px}
.card-back{left:310px;background:radial-gradient(ellipse at 50% 45%,var(--red-light),var(--red) 55%,var(--red-deep));display:flex;align-items:center;justify-content:center}
.card-front .brand{position:absolute;left:18px;top:22px}
.card-front .brand .word{font-size:22px}
.card-front .brand .sub{font-size:5.5px}
.card-front .brand .dot{width:7px;height:7px;margin-top:4px}
.card-back .brand .word{font-size:26px}
.card-back .brand .sub{font-size:6.5px}
.card-back .brand .dot{width:8px;height:8px;margin-top:5px}
.holder{position:absolute;right:16px;top:24px;text-align:right;font-size:6px;color:var(--grey)}
.holder .person{font-size:9px;font-weight:700;color:var(--red)}
.contact{list-style:none;font-size:6px;color:var(--grey);line-height:1.35}
.contact .addr{font-weight:700;color:var(--ink)}
.contact .ico{display:inline-block;width:5px;height:5px;border-radius:1px;background:var(--red);margin-right:3px;vertical-align:middle}
.card-front .contact{position:absolute;left:18px;top:68px}
.card-front .band{height:36px}
.card-front .web{bottom:10px;font-size:6px;right:14px}

/* envelope back */
.envelope-back{left:40px;top:205px;width:560px;height:240px}
.envelope-back .folds{position:absolute;left:0;top:0;width:100%;height:100%}
.envelope-back .flap{position:absolute;left:0;top:0;width:100%;height:120px;background:linear-gradient(180deg,var(--red-light),var(--red) 55%,var(--red-deep))}
.envelope-back .brand{position:absolute;left:50%;top:44px;transform:translateX(-50%)}
.envelope-back .brand .word{font-size:28px}
.envelope-back .brand .sub{font-size:7px}
.envelope-back .brand .dot{width:9px;height:9px;margin-top:5px}

/* window envelope */
.envelope-front{left:40px;top:468px;width:560px;height:300px}
.envelope-front .brand{position:absolute;left:40px;top:46px}
.envelope-front .brand .word{font-size:28px}
.envelope-front .brand .sub{font-size:7px}
.envelope-front .brand .dot{width:9px;height:9px;margin-top:5px}
.address-window{position:absolute;left:58px;top:120px;width:260px;height:80px;border-radius:12px;background:#f1f1f2;border:1px solid #dcdcdd;box-shadow:inset 0 1px 4px rgba(0,0,0,.12)}
.envelope-front .band{height:60px}
.envelope-front .web{bottom:24px}

/* letterhead */
.letterhead{left:640px;top:36px;width:520px;height:736px}
.letterhead .brand{position:absolute;left:46px;top:82px}
.letterhead .brand .word{font-size:28px}
.letterhead .brand .sub{font-size:7px}
.letterhead .brand .dot{width:9px;height:9px;margin-top:5px}
.letterhead .contact{position:absolute;left:404px;top:26px}
.letter{position:absolute;left:60px;top:165px;width:410px;font-size:8.8px;line-height:1.5;color:#333}
.letter .date{margin-bottom:16px}
.recipient{margin-bottom:22px;line-height:1.35}
.recipient strong{font-weight:700;color:var(--ink);font-size:10.5px}
.letter p.body{text-align:justify;margin-bottom:12px}
.closing{margin-top:14px}
.signature{display:block;margin:12px 0 6px}
.sender strong{font-weight:700;color:var(--ink)}
.letterhead .band{height:50px}
.letterhead .web{bottom:18px}
</style>
</head>
<body>

<section class="sheet card card-front">
  <div class="brand"><div class="name"><span class="word">veltrix</span><span class="sub">PROMOTIONS GROUP</span></div><span class="dot"></span></div>
  <div class="holder"><div class="person">Your Name</div><div>Position</div><div>(123) 456 7890</div></div>
  <ul class="contact">
    <li class="addr">123, Your Street,</li>
    <li class="addr">Your City, Country, 123.</li>
    <li><span class="ico"></span>(123) 456 7890</li>
    <li><span class="ico"></span>(123) 456 7890</li>
    <li><span class="ico"></span>info@veltrix.com</li>
  </ul>
  <div class="band" role="img" aria-label="Red and grey wave band along the card foot"></div>
  <span class="web">www.veltrix.com</span>
</section>

<section class="sheet card card-back">
  <div class="brand on-red"><div class="name"><span class="word">veltrix</span><span class="sub">PROMOTIONS GROUP</span></div><span class="dot"></span></div>
</section>

<section class="sheet envelope-back">
  <svg class="folds" viewBox="0 0 560 240" preserveAspectRatio="none" aria-hidden="true">
    <line x1="0" y1="240" x2="250" y2="120" stroke="#555" stroke-width=".8"/>
    <line x1="560" y1="240" x2="330" y2="120" stroke="#555" stroke-width=".8"/>
  </svg>
  <div class="flap" role="img" aria-label="Curved red envelope flap"></div>
  <div class="brand on-red"><div class="name"><span class="word">veltrix</span><span class="sub">PROMOTIONS GROUP</span></div><span class="dot"></span></div>
</section>

<section class="sheet envelope-front">
  <div class="brand"><div class="name"><span class="word">veltrix</span><span class="sub">PROMOTIONS GROUP</span></div><span class="dot"></span></div>
  <div class="address-window"></div>
  <div class="band" role="img" aria-label="Red and grey wave band along the envelope foot"></div>
  <span class="web">www.veltrix.com</span>
</section>

<section class="sheet letterhead">
  <ul class="contact">
    <li class="addr">123, Your Street,</li>
    <li class="addr">Your City, Country, 123.</li>
    <li><span class="ico"></span>(123) 456 7890</li>
    <li><span class="ico"></span>(123) 456 7890</li>
    <li><span class="ico"></span>info@veltrix.com</li>
  </ul>
  <div class="brand"><div class="name"><span class="word">veltrix</span><span class="sub">PROMOTIONS GROUP</span></div><span class="dot"></span></div>

  <article class="letter">
    <p class="date">March 4, 2011</p>
    <p class="recipient"><strong>Mr Colin Ashdown</strong><br>Managing Director<br><strong>Quellmark Holdings</strong><br>48 Harbor Lane<br>Brookfield, OR 97410</p>
    <p class="body">Lorem Ipsum is simply dummy text of the printing and typesetting industry. Lorem Ipsum has been the industry's standard dummy text ever since the 1500s, when an unknown printer took a galley of type and scrambled it to make a type specimen book. It has survived not only five centuries, but also the leap into electronic typesetting, remaining essentially unchanged. It was popularised in the 1960s with the release of Typeline sheets containing Lorem Ipsum passages, and more recently with desktop publishing software like Folio Layout including versions of Lorem Ipsum.</p>
    <p class="body">Contrary to popular belief, Lorem Ipsum is not simply random text. It has roots in a piece of classical Latin literature from 45 BC, making it over 2000 years old. Edwin Harrowgate, a Latin professor at Larkmoor College, looked up one of the more obscure Latin words, consectetur, from a Lorem Ipsum passage, and going through the cites of the word in classical literature, discovered the undoubtable source. Lorem Ipsum comes from sections 1.10.32 and 1.10.33 of "de Finibus Bonorum et Malorum" (The Extremes of Good and Evil) by Aurelian, written in 45 BC. This book is a treatise on the theory of ethics, very popular during the Renaissance. The first line of Lorem Ipsum, "Lorem ipsum dolor sit amet..", comes from a line in section 1.10.32.</p>
    <p class="closing">Thank You for being one of our valued customers.</p>
    <svg class="signature" width="120" height="36" viewBox="0 0 120 36" aria-hidden="true">
      <path d="M6,28 C14,6 26,4 22,22 C20,32 34,12 40,18 C46,24 52,10 60,16 C70,22 90,8 118,4" fill="none" stroke="var(--ink)" stroke-width="1.2"/>
    </svg>
    <p class="sender"><strong>Marko Delan</strong><br>President<br>Brookfield Fabrication</p>
  </article>

  <div class="band" role="img" aria-label="Red and grey wave band along the page foot"></div>
  <span class="web">www.veltrix.com</span>
</section>

</body>
</html>
```